Website needed for a specialty chemical company!

We are looking for a new website design to replace our current site.
We are a woman and minority owned, specialty chemical company that specializes in environmentally safe products and chemicals, or what we like to call "green solutions".
Our clientele are mostly companies in the construction business, as our current products consist of asphalt release agents, tar/asphalt cleaners, concrete form release agents, concrete removers and environmentally safe detergents. If a special product is needed, our formulation team can also custom create chemicals and products for your industry or company.
We are looking for at least three pages total. A home page, a products page that lists our products and also provides additional product information and a contact us page.
Our current site is at: www.brovane-labs.com
This will give you a general idea of what type of content will be on our site.
We are very open to content ideas, pictures, colors and CREATIVITY.
We would like to stress that we are "environmentally friendly" and would like to use "earthy" tones and greens if possible.
We also prefer a more modern website design as opposed to something traditional. An example of a site design that we like is: http://www.plumrit.com/
The design does not have to follow this, this is just a site look and feel that we liked. :)
Updates
Target Market(s)
Construction Companies, Truckers
Industry/Entity Type
It Company
Coding
Coded - Design and coding required
Number of Pages Required
3 page
Font styles to use
Look and feel
Each slider illustrates characteristics of the customer's brand and the style your logo design should communicate.

```html
<!DOCTYPE html>
<html lang="en">
<head>
<meta charset="utf-8">
<title>Brovane Labs — Green Solutions</title>
<link rel="stylesheet" href="https://fonts.googleapis.com/css2?family=Raleway:wght@400;500;600&family=Open+Sans:wght@400;600&family=Roboto:wght@400;500&family=Oswald:wght@300;400&display=swap">
<style>
:root{
  --green:#0f7a45;
  --green-dark:#0c6a3b;
  --ink:#2b2b2b;
  --muted:#555;
  --light:#f2f2f2;
  --rule:#cfcfcf;
  --hero-a:#7b8fa6;
  --hero-b:#3e5168;
  --footer-bar:#1b1b1b;
}
*{margin:0;padding:0;box-sizing:border-box}
html,body{width:782px;height:1200px;overflow:hidden;background:#fff}
body{position:relative;font-family:"Open Sans",Arial,sans-serif;color:var(--ink)}
.abs{position:absolute}

/* header */
.site-header{left:0;top:0;width:782px;height:82px;background:#fff}
.brand{left:56px;top:22px;display:flex;align-items:center;gap:8px}
.brand-mark{width:26px;height:26px;background:var(--green)}
.brand-name{font-family:"Roboto",sans-serif;font-weight:500;font-size:15px;color:var(--green);letter-spacing:.5px}
.nav a{position:absolute;top:34px;font-family:"Roboto",sans-serif;font-size:10px;color:var(--ink);text-decoration:none;letter-spacing:.2px}
.nav a.active{color:var(--green)}
.nav .divider{position:absolute;left:676px;top:32px;width:1px;height:16px;background:#333}
.cart{left:682px;top:33px;font-family:"Roboto",sans-serif;font-size:10px;display:flex;align-items:center;gap:3px}

/* hero */
.hero{left:0;top:82px;width:782px;height:337px;background:radial-gradient(ellipse at 50% 45%,var(--hero-a),var(--hero-b))}
.hero-title{left:0;top:136px;width:782px;text-align:center;font-family:"Raleway",sans-serif;font-weight:500;font-size:19px;color:#fff;letter-spacing:.3px}
.product-photo{position:absolute;width:97px;height:97px;border-radius:50%;border:3px solid #fff;top:203px}
.product-name{position:absolute;top:320px;width:140px;text-align:center;font-family:"Raleway",sans-serif;font-size:12.5px;color:#fff}
.slide-arrow{top:226px}

/* welcome */
.welcome-title{left:0;top:463px;width:782px;text-align:center;font-family:"Raleway",sans-serif;font-size:16px;font-weight:500;color:var(--ink)}
.welcome-title span{color:var(--green);margin-left:6px}
.welcome-text{left:62px;top:494px;width:658px;text-align:center;font-size:8.6px;line-height:17.5px;color:var(--muted)}

/* why */
.why{left:0;top:572px;width:782px;height:229px;background:var(--light)}
.why-title{left:0;top:591px;width:782px;text-align:center;font-family:"Raleway",sans-serif;font-size:13px;font-weight:500}
.why-title span{color:var(--green)}
.feature{position:absolute;top:632px;width:200px;text-align:center}
.feature-icon{width:70px;height:70px;margin:0 auto;border-radius:50%;background:var(--green);border:3px solid #fff;box-shadow:0 0 0 1px #d4d4d4;display:flex;align-items:center;justify-content:center}
.feature h3{margin-top:15px;font-family:"Roboto",sans-serif;font-weight:400;font-size:12.5px;color:var(--green)}
.feature p{margin-top:8px;font-size:8.3px;line-height:16.5px;color:#333}

/* blog & news */
.section-label{font-family:"Roboto",sans-serif;font-size:10px;color:var(--green);letter-spacing:.3px}
.section-rule{height:1px;background:var(--rule)}
.blog-card{position:absolute;top:864px;width:152px;height:117px;background:#fff;box-shadow:0 1px 2px rgba(0,0,0,.25)}
.blog-card .thumb{width:152px;height:91px}
.blog-card p{text-align:center;font-size:8.3px;margin-top:8px;color:#222}
.news-panel{left:396px;top:858px;width:334px;height:137px;background:#f6f6f6}
.news-item{position:absolute;left:400px;width:326px}
.news-date{position:absolute;left:0;top:0;width:40px;height:45px;background:#fff;border:1px solid #ddd;text-align:center}
.news-date b{display:block;font-family:"Roboto",sans-serif;font-size:13px;font-weight:500;margin-top:5px}
.news-date i{display:block;font-style:normal;font-size:7.5px;color:#888;border-top:1px solid #ddd;margin-top:4px;padding-top:3px}
.news-item h4{position:absolute;left:47px;top:0;font-family:Arial,sans-serif;font-weight:400;font-size:7.5px;color:var(--green)}
.news-item p{position:absolute;left:47px;top:12px;width:280px;font-family:Arial,sans-serif;font-size:6.4px;line-height:11.4px;color:#777}
.news-sep{left:402px;top:926px;width:320px;border-top:1px dotted #888}

/* footer */
.site-footer{left:0;top:1001px;width:782px;height:154px;background:var(--green)}
.footer-head{position:absolute;top:1025px;font-family:"Oswald",sans-serif;font-weight:300;font-size:12.5px;color:#fff;letter-spacing:.2px}
.footer-text{position:absolute;font-family:Arial,sans-serif;font-size:7.8px;line-height:12px;color:#fff}
.email-field{left:66px;top:1080px;width:141px;height:20px;background:#f3f3f3;border:1px solid #ccc;font-size:6.5px;color:#777;padding:5px 7px}
.subscribe{left:66px;top:1108px;width:62px;height:19px;background:#eee;border-radius:2px;font-family:Arial,sans-serif;font-size:7.3px;font-weight:bold;color:#333;text-align:center;line-height:19px;letter-spacing:.3px}
.tweet-dot{left:261px;top:1060px;width:10px;height:10px;border-radius:50%;background:#fff}
.social{position:absolute;left:636px;display:flex;align-items:center;gap:10px;font-family:Arial,sans-serif;font-size:8px;color:#fff}
.social-dot{width:21px;height:21px;border-radius:50%;border:1px solid rgba(255,255,255,.8)}
.footer-bar{left:0;top:1155px;width:782px;height:45px;background:var(--footer-bar)}
.copyright{left:0;top:1170px;width:782px;text-align:center;font-family:Arial,sans-serif;font-size:8px;color:#fff}
</style>
</head>
<body>

<header class="site-header abs">
  <div class="brand abs"><span class="brand-mark"></span><span class="brand-name">BROVANE LABS</span></div>
  <nav class="nav">
    <a class="active" style="left:337px">HOME</a>
    <a style="left:386px">PRODUCTS</a>
    <a style="left:458px">CONTACT US</a>
    <a style="left:538px">MY ACCOUNT</a>
    <a style="left:639px">LOGIN</a>
    <span class="divider"></span>
  </nav>
  <div class="cart abs">
    <svg width="11" height="10" viewBox="0 0 11 10"><path d="M0 1h2l1.5 5h6l1-3.5H3" fill="none" stroke="#0f7a45" stroke-width="1.4"/><circle cx="4.3" cy="8.5" r="1" fill="#0f7a45"/><circle cx="8.7" cy="8.5" r="1" fill="#0f7a45"/></svg>
    <span>: 0.00</span>
  </div>
</header>

<section class="hero abs" role="img" aria-label="Background photo of a chemical structure diagram drawn in dark ink"></section>
<h1 class="hero-title abs">OUR PRODUCTS ARE USED IN..</h1>
<div class="product-photo" style="left:97px;background:#b9b5aa" role="img" aria-label="Photo of absorbent granules"></div>
<div class="product-photo" style="left:258px;background:#6b6d62" role="img" aria-label="Photo of an asphalt paving machine at work"></div>
<div class="product-photo" style="left:413px;background:#d9d6cf" role="img" aria-label="Photo of a product drum label"></div>
<div class="product-photo" style="left:569px;background:#9aa88f" role="img" aria-label="Photo of a green dump truck"></div>
<div class="product-name" style="left:74px">FlowSorb™</div>
<div class="product-name" style="left:235px">PaveGlide™</div>
<div class="product-name" style="left:393px">PitchLift™</div>
<div class="product-name" style="left:551px">FrostGlide™</div>
<svg class="slide-arrow abs" style="left:27px" width="18" height="38" viewBox="0 0 18 38"><path d="M17 1L1 19l16 18" fill="none" stroke="#fff" stroke-width="1.3"/></svg>
<svg class="slide-arrow abs" style="left:736px" width="18" height="38" viewBox="0 0 18 38"><path d="M1 1l16 18L1 37" fill="none" stroke="#fff" stroke-width="1.3"/></svg>

<h2 class="welcome-title abs">WELCOME TO<span>BROVANE LABS</span></h2>
<p class="welcome-text abs">Lorem Ipsum has been the industry's standard dummy text ever since the 1500s, when an unknown printer took a galley of type and scrambled it to make a type specimen book. It has survived not only five centuries, but also the leap into electronic typesetting, remaining essentially unchanged. It was popularised in the 1960s with the release of Lettrano sheets containing Lorem Ipsum passages, and more recently with desktop publishing software</p>

<section class="why abs"></section>
<h2 class="why-title abs">WHY BROVANE <span>LABS™?</span></h2>
<div class="feature" style="left:67px">
  <div class="feature-icon"><svg width="30" height="24" viewBox="0 0 30 24" fill="#fff"><circle cx="8" cy="5" r="3.5"/><circle cx="15" cy="4" r="4"/><circle cx="22" cy="5" r="3.5"/><path d="M2 16c0-4 3-6 6-6s4 1 4 1-2 2-2 5zM28 16c0-4-3-6-6-6s-4 1-4 1 2 2 2 5z"/><path d="M8 22c0-6 3-9 7-9s7 3 7 9z"/></svg></div>
  <h3>Safe To Use</h3>
  <p>Brovane products contain no dangerous chemicals<br>or additives and are safe around you,</p>
</div>
<div class="feature" style="left:292px">
  <div class="feature-icon"><svg width="26" height="24" viewBox="0 0 26 24" fill="#fff"><path d="M25 1L1 11l7 3 13-10-10 12v7l4-5 5 3z"/></svg></div>
  <h3>Effective</h3>
  <p>Brovane products not only do their job, they do<br>their job well.</p>
</div>
<div class="feature" style="left:516px">
  <div class="feature-icon"><svg width="16" height="28" viewBox="0 0 16 28"><text x="8" y="23" text-anchor="middle" font-family="Roboto,sans-serif" font-size="26" font-weight="500" fill="#fff">$</text></svg></div>
  <h3>Economically Priced</h3>
  <p>Brovane Labs™ offers cost effective solutions<br>on the job, around the home and for you.</p>
</div>

<div class="section-label abs" style="left:60px;top:834px">RECENTLY &nbsp;BLOG</div>
<svg class="abs" style="left:359px;top:834px" width="15" height="9" viewBox="0 0 15 9"><path d="M5 1L1 4.5 5 8M10 1l4 3.5L10 8" fill="none" stroke="#333" stroke-width="1.2"/></svg>
<div class="section-rule abs" style="left:58px;top:851px;width:310px"></div>
<article class="blog-card" style="left:58px">
  <div class="thumb" style="background:linear-gradient(135deg,#c7d3de,#6f8eae)" role="img" aria-label="Photo of a scientist using a microscope"></div>
  <p>Lorem Ipsum is simply</p>
</article>
<article class="blog-card" style="left:217px">
  <div class="thumb" style="background:linear-gradient(135deg,#1e5fc4,#0c2f7a)" role="img" aria-label="Photo of a test tube over a blue molecule backdrop"></div>
  <p>Lorem Ipsum is simply</p>
</article>

<div class="section-label abs" style="left:400px;top:834px">LATEST NEWS</div>
<div class="section-rule abs" style="left:398px;top:851px;width:332px"></div>
<div class="news-panel abs"></div>
<div class="news-item" style="top:864px">
  <div class="news-date"><b>20</b><i>mar</i></div>
  <h4>NEWS HEADLINE HERE</h4>
  <p>Lorem ipsum dolor sit amet, consectetur adipisicing elit, sed do eiusmod tempor incididunt ut labore et dolore magna aliqua. Ut enim ad minim veniam, quis nostrud exercitation ullamco laboris nisi ut aliquip ex ea commodo consequat.</p>
</div>
<div class="news-sep abs"></div>
<div class="news-item" style="top:938px;left:402px">
  <div class="news-date"><b>20</b><i>mar</i></div>
  <h4>NEWS HEADLINE HERE</h4>
  <p>Lorem ipsum dolor sit amet, consectetur adipisicing elit, sed do eiusmod tempor incididunt ut labore et dolore magna aliqua. Ut enim ad minim veniam, quis nostrud exercitation ullamco laboris nisi ut aliquip ex ea commodo consequat.</p>
</div>

<footer class="site-footer abs"></footer>
<div class="footer-head" style="left:66px">NEWSLETTERS SIGN UP</div>
<p class="footer-text" style="left:66px;top:1054px;font-size:7px;line-height:10.5px">Sign up for our daily email by entering<br>your information below</p>
<div class="email-field abs">Email address</div>
<div class="subscribe abs">SUBSCRIBE</div>

<div class="footer-head" style="left:260px">LATEST TWEET</div>
<span class="tweet-dot abs"></span>
<p class="footer-text" style="left:278px;top:1062px">Featured Workspace : Studio Pine</p>
<p class="footer-text" style="left:279px;top:1079px;font-style:italic;font-size:7.3px">lnk.to/8TrwQe"</p>
<p class="footer-text" style="left:278px;top:1096px">10 hours ago</p>

<div class="footer-head" style="left:454px">GET IN TOUCH</div>
<p class="footer-text" style="left:456px;top:1054px">Address : 1420 Meadow Ridge Rd,<br>Fairlawn, OH</p>
<p class="footer-text" style="left:456px;top:1089px">Phone : 555 014 2287</p>
<p class="footer-text" style="left:456px;top:1111px">Email : info@brovane-labs.com</p>

<div class="footer-head" style="left:635px">FOLLOW US ON</div>
<div class="social" style="top:1057px"><span class="social-dot"></span>Plazaline</div>
<div class="social" style="top:1085px"><span class="social-dot"></span>Quillpost</div>
<div class="social" style="top:1114px"><span class="social-dot"></span>Lensfeed</div>

<div class="footer-bar abs"></div>
<p class="copyright abs">Copyright © 2015. All Rights Reserved</p>

</body>
</html>
```